Harborline Keys Realty business card design

Looking for an upscale and clean business card design and updated logo. I sell to a very high-end south Florida real estate market.
Target Market(s)
High-end real estate in south Florida real estate market
Industry/Entity Type
Real Estate Agent
Contact Information for Business Card
Harborline Keys Realty, Inc
738 West Pinecrest Ave, Suite 410/520, Fort Lauderdale, FL 33318
Carl Whitmore - Broker/Owner
954-555-0172 Direct
carlhomes@mailvista.example
Website: StayPinecrest.example
Font styles to use
Other font styles liked:
- Copperplate Gothic, Georgia, etc.
Requirements
Must have
- My photo, company name, my name and title, all info stated in Details above
Nice to have
- Luxury home design element, waterfront

```html
<!DOCTYPE html>
<html lang="en">
<head>
<meta charset="utf-8">
<title>Harborline Keys Realty – Business Card</title>
<link rel="stylesheet" href="https://fonts.googleapis.com/css2?family=Gelasio:wght@400&family=Montserrat:wght@400;600;700&display=swap">
<style>
  :root {
    --page: #e4e4e4;
    --white: #ffffff;
    --ink: #1c1c1c;
    --gold: #f2b91c;
    --gold-light: #f5c93a;
    --charcoal: #3a3a3a;
    --charcoal-deep: #1f1f1f;
    --mark-grey: #8e8e8e;
  }
  * { box-sizing: border-box; margin: 0; padding: 0; }
  html, body { width: 1200px; height: 1200px; overflow: hidden; }
  body { background: var(--page); position: relative; font-family: "Montserrat", sans-serif; color: var(--ink); }

  .card {
    position: absolute; left: 160px; width: 880px; height: 503px;
    border-radius: 26px; overflow: hidden;
  }
  .card-front { top: 60px; background: var(--white); }
  .card-back { top: 637px; background: linear-gradient(160deg, #4a4a4a 0%, #2a2a2a 45%, var(--charcoal-deep) 100%); }

  .brand { position: absolute; display: flex; align-items: center; }
  .brand-dot { border-radius: 50%; background: var(--gold); flex: none; }
  .brand-name { font-family: "Gelasio", Georgia, serif; font-weight: 400; white-space: nowrap; }

  .card-front .brand { left: 44px; top: 118px; gap: 18px; }
  .card-front .brand-dot { width: 72px; height: 72px; }
  .card-front .brand-name { font-size: 23px; color: var(--ink); }

  .address {
    position: absolute; left: 66px; top: 296px;
    font-size: 17px; line-height: 22px; font-variant: small-caps; letter-spacing: 0.5px;
  }
  .contact { position: absolute; left: 66px; font-size: 17px; display: flex; align-items: center; gap: 9px; letter-spacing: 0.3px; }
  .contact svg { width: 15px; height: 15px; fill: var(--gold); flex: none; }
  .contact-phone { top: 378px; }
  .contact-email { top: 403px; font-size: 14.5px; text-transform: uppercase; }

  .web-band {
    position: absolute; left: 0; top: 465px; width: 496px; height: 38px;
    background: linear-gradient(90deg, var(--gold), var(--gold-light));
    clip-path: polygon(0 0, 100% 0, 94% 100%, 0 100%);
  }
  .web-address {
    position: absolute; left: 60px; top: 474px;
    font-size: 16px; font-weight: 700; letter-spacing: 5.5px; text-transform: uppercase; color: var(--ink);
  }

  .name-panel {
    position: absolute; left: 482px; top: 383px; width: 398px; height: 120px;
    background: var(--charcoal);
    clip-path: polygon(17% 0, 100% 0, 100% 100%, 0 100%);
  }
  .agent-name {
    position: absolute; left: 560px; width: 320px; top: 406px; text-align: center;
    font-size: 33px; font-weight: 700; color: var(--gold); letter-spacing: 1px; text-transform: uppercase; white-space: nowrap;
  }
  .agent-title {
    position: absolute; left: 560px; width: 320px; top: 449px; text-align: center;
    font-size: 17px; color: var(--white); font-variant: small-caps; letter-spacing: 1px;
  }

  .agent-photo {
    position: absolute; left: 561px; top: 11px; width: 319px; height: 363px;
    background: linear-gradient(180deg, #f3f3f3 0%, #e9d3d6 30%, #3a5a9c 60%, #2c477f 100%);
  }

  .card-back .brand { left: 176px; top: 205px; gap: 20px; }
  .card-back .brand-dot { width: 92px; height: 92px; }
  .card-back .brand-name { font-size: 32px; color: var(--mark-grey); }
</style>
</head>
<body>

<section class="card card-front">
  <div class="brand">
    <span class="brand-dot"></span>
    <span class="brand-name">Harborline Keys Realty, Inc.</span>
  </div>

  <p class="address">738 West Pinecrest Ave<br>Suite 410/520<br>Fort Lauderdale, FL 33318</p>

  <p class="contact contact-phone">
    <svg viewBox="0 0 24 24" aria-hidden="true"><path d="M6.6 10.8c1.4 2.8 3.8 5.1 6.6 6.6l2.2-2.2c.3-.3.7-.4 1-.2 1.1.4 2.3.6 3.6.6.6 0 1 .4 1 1V20c0 .6-.4 1-1 1C10.6 21 3 13.4 3 4c0-.6.4-1 1-1h3.5c.6 0 1 .4 1 1 0 1.3.2 2.5.6 3.6.1.3 0 .7-.2 1l-2.3 2.2z"/></svg>
    954-555-0172
  </p>
  <p class="contact contact-email">
    <svg viewBox="0 0 24 24" aria-hidden="true"><path d="M2 5h20v14H2z M2 5l10 7 10-7" /></svg>
    carlhomes@mailvista.example
  </p>

  <div class="web-band"></div>
  <p class="web-address">StayPinecrest.example</p>

  <div class="agent-photo" role="img" aria-label="Portrait photo of Carl Whitmore in a blue blazer and pink shirt"></div>

  <div class="name-panel"></div>
  <h1 class="agent-name">Carl Whitmore</h1>
  <p class="agent-title">Broker/Owner</p>
</section>

<section class="card card-back">
  <div class="brand">
    <span class="brand-dot"></span>
    <span class="brand-name">Harborline Keys Realty, Inc.</span>
  </div>
</section>

</body>
</html>
```